I'm an electrician and the name of my company is called Brisk 'N' Bright Electrical. I require a professional business card that speaks to my clients, I also need it to be innovative and modern. We do maintenance & service work for domestic and commercial premises.

Industry/Entity Type

Electrical

Contact Information for Business Card

Must have the name of my company Brisk 'N' Bright Electrical, my name Darren Kolovos and my contact details 0427 381 592 and company email address Brisknbrightelectrical@mailvane.com and/or website Brisknbrightelectrical.com.au

Logo Text

Brisk 'N' Bright Electrical (If possible)

Colors
33a6d7
0592cd
3176b5

```html
<!DOCTYPE html>
<html lang="en">
<head>
<meta charset="utf-8">
<title>Brisk 'N' Bright Electrical — Business Card</title>
<link href="https://fonts.googleapis.com/css2?family=Arimo:wght@400;700&display=swap" rel="stylesheet">
<style>
  :root {
    --sky: #33a6d7;
    --azure: #0592cd;
    --royal: #3176b5;
    --deep: #2a66a8;
    --paper: #ffffff;
    --ink: #14202e;
    --stage: #e9ecef;
  }
  * { box-sizing: border-box; margin: 0; padding: 0; }
  html, body {
    width: 1200px; height: 900px; overflow: hidden;
    background: var(--stage);
    font-family: "Arimo", Arial, sans-serif;
  }
  .sheet {
    position: relative; width: 1200px; height: 900px;
  }
  .card {
    position: absolute; left: 250px; width: 700px; height: 400px;
    overflow: hidden;
    box-shadow: 0 8px 24px rgba(0,0,0,0.18);
  }
  .card--front { top: 40px; background: var(--paper); }
  .card--back {
    top: 470px;
    background: linear-gradient(160deg, var(--sky) 0%, var(--royal) 55%, var(--deep) 100%);
  }
  .card__panel { position: absolute; inset: 0; width: 100%; height: 100%; }

  .brand {
    position: absolute; display: flex; align-items: center; gap: 14px;
    font-weight: 700; letter-spacing: 1px; white-space: nowrap;
  }
  .brand__dot { border-radius: 50%; flex: none; }
  .card--front .brand { left: 120px; top: 112px; font-size: 44px; color: var(--ink); }
  .card--front .brand__dot { width: 34px; height: 34px; background: var(--ink); }
  .card--back .brand { left: 50%; top: 50%; transform: translate(-50%, -50%); font-size: 58px; color: var(--paper); }
  .card--back .brand__dot { width: 44px; height: 44px; background: var(--paper); }

  .holder {
    position: absolute; left: 110px; top: 300px;
    font-weight: 700; font-size: 32px; color: var(--royal); letter-spacing: 0.5px;
  }
  .contacts {
    position: absolute; left: 392px; top: 196px;
    list-style: none; color: var(--paper); font-size: 15px; white-space: nowrap;
  }
  .contacts__item { display: flex; align-items: center; gap: 10px; margin-bottom: 11px; }
  .contacts__icon { width: 18px; height: 18px; flex: none; }
</style>
</head>
<body>
<main class="sheet">
  <section class="card card--front" aria-label="Card front">
    <svg class="card__panel" viewBox="0 0 700 400" preserveAspectRatio="none" aria-hidden="true">
      <defs>
        <linearGradient id="panelBlue" x1="0" y1="0" x2="0.4" y2="1">
          <stop offset="0" stop-color="#33a6d7"/>
          <stop offset="0.5" stop-color="#3176b5"/>
          <stop offset="1" stop-color="#2a66a8"/>
        </linearGradient>
      </defs>
      <polygon points="105,0 700,0 700,400 490,400" fill="url(#panelBlue)"/>
    </svg>
    <div class="brand"><span class="brand__dot"></span>BRISK 'N' BRIGHT</div>
    <p class="holder">Darren Kolovos</p>
    <ul class="contacts">
      <li class="contacts__item">
        <svg class="contacts__icon" viewBox="0 0 18 18" aria-hidden="true"><rect x="5" y="1.5" width="8" height="15" rx="1.5" fill="none" stroke="#fff" stroke-width="1.4"/><line x1="8" y1="14" x2="10" y2="14" stroke="#fff" stroke-width="1.2"/></svg>
        0427 381 592
      </li>
      <li class="contacts__item">
        <svg class="contacts__icon" viewBox="0 0 18 18" aria-hidden="true"><g fill="none" stroke="#fff" stroke-width="1.3"><circle cx="9" cy="9" r="7.5"/><ellipse cx="9" cy="9" rx="3.2" ry="7.5"/><line x1="1.5" y1="9" x2="16.5" y2="9"/></g></svg>
        Brisknbrightelectrical.com.au
      </li>
      <li class="contacts__item">
        <svg class="contacts__icon" viewBox="0 0 18 18" aria-hidden="true"><g fill="none" stroke="#fff" stroke-width="1.3"><rect x="1.5" y="4" width="15" height="10"/><polyline points="1.5,4 9,10 16.5,4"/></g></svg>
        Brisknbrightelectrical@mailvane.com
      </li>
    </ul>
  </section>

  <section class="card card--back" aria-label="Card back">
    <div class="brand"><span class="brand__dot"></span>BRISK 'N' BRIGHT</div>
  </section>
</main>
</body>
</html>
```